Business Card Design Project

Need a business card designed for a horse racing/gambling centered company.
Company name is BrightQuill.com.au
Company colours are similar to those in the logo.
Something clean and modern , designer given liberty to be creative.
Incorporate the logo is preferred.
Single or Double Sided fine
Must include :
Name
Mobile Number
Email Address
Reason: Apologies, I have been traveling unexpectedly with business and just need the extra two days to reply and give feedback before making a decision.
Industry/Entity Type
Business

```html
<!DOCTYPE html>
<html lang="en">
<head>
<meta charset="utf-8">
<title>BrightQuill.com.au Business Card</title>
<link href="https://fonts.googleapis.com/css2?family=Open+Sans:wght@300;400;600&display=swap" rel="stylesheet">
<style>
  :root {
    --teal: #1aa39a;
    --teal-dark: #128a82;
    --green: #9fd22a;
    --ink: #111111;
    --text: #1c1c1c;
    --paper: #ffffff;
    --stage: #e9e6e2;
    --divider: #e3e6e6;
  }
  * { margin: 0; padding: 0; box-sizing: border-box; }
  html, body {
    width: 1200px; height: 900px; overflow: hidden;
    background: var(--stage);
    font-family: "Open Sans", Arial, sans-serif;
  }
  .sheet {
    width: 1200px; height: 900px;
    display: flex; flex-direction: column; align-items: center; justify-content: center;
    gap: 30px;
  }
  .card {
    position: relative;
    width: 700px; height: 400px;
    overflow: hidden;
    box-shadow: 0 6px 18px rgba(0,0,0,.18);
  }
  .card--back { background: var(--teal); }
  .card--back svg { display: block; }

  .card--front { background: var(--paper); }
  .brand-block {
    position: absolute; left: 0; top: 0; width: 330px; height: 350px;
    display: flex; flex-direction: column; align-items: center; justify-content: center;
  }
  .brand-mark {
    width: 84px; height: 84px; border-radius: 50%;
    background: var(--teal); margin-bottom: 16px;
  }
  .brand-name {
    font-weight: 300; font-size: 46px; line-height: 1; color: var(--teal);
    letter-spacing: -1px;
  }
  .brand-domain {
    font-weight: 300; font-size: 18px; color: var(--teal);
    align-self: flex-start; margin-left: 58px; margin-top: 2px;
  }
  .divider {
    position: absolute; left: 335px; top: 40px; width: 1px; height: 290px;
    background: var(--divider);
  }
  .contact-block {
    position: absolute; left: 365px; top: 70px; color: var(--text);
  }
  .person-name { font-weight: 600; font-size: 27px; line-height: 1.1; }
  .person-role { font-size: 18px; margin-bottom: 24px; }
  .address { font-size: 17px; line-height: 1.3; margin-bottom: 16px; }
  .contact-list { list-style: none; font-size: 17px; line-height: 1.45; }
  .contact-list li { display: flex; align-items: center; gap: 12px; }
  .contact-list svg { width: 16px; height: 16px; flex: none; }
  .band { position: absolute; bottom: 0; height: 48px; }
  .band--teal { left: 0; width: 495px; background: var(--teal); }
  .band--green { left: 503px; right: 0; height: 56px; background: var(--green); }
</style>
</head>
<body>
<main class="sheet">

  <section class="card card--back" aria-label="Card back">
    <svg width="700" height="400" viewBox="0 0 700 400">
      <defs>
        <linearGradient id="bandShade" x1="0" y1="0" x2="1" y2="0">
          <stop offset="0" stop-color="#0c0c0c"/>
          <stop offset="0.55" stop-color="#2a2a2a"/>
          <stop offset="1" stop-color="#111"/>
        </linearGradient>
      </defs>
      <circle class="faint-ring" cx="590" cy="95" r="135" fill="#ffffff" fill-opacity="0.07"/>
      <polygon class="diagonal-band" points="0,292 700,212 700,282 0,362" fill="url(#bandShade)"/>
      <circle class="brand-mark" cx="90" cy="180" r="42" fill="#ffffff"/>
      <text x="150" y="198" fill="#ffffff" font-family="Open Sans, sans-serif" font-weight="300" font-size="52" letter-spacing="-1">BrightQuill</text>
      <text x="206" y="222" fill="#ffffff" font-family="Open Sans, sans-serif" font-weight="300" font-size="18">.com.au</text>
      <text x="420" y="268" fill="#ffffff" font-family="Open Sans, sans-serif" font-size="18" transform="rotate(-6.5 420 268)">www.brightquill.com.au</text>
    </svg>
  </section>

  <section class="card card--front" aria-label="Card front">
    <div class="brand-block">
      <div class="brand-mark"></div>
      <div class="brand-name">BrightQuill</div>
      <div class="brand-domain">.com.au</div>
    </div>
    <div class="divider"></div>
    <div class="contact-block">
      <p class="person-name">Daniel Hartley</p>
      <p class="person-role">Owner</p>
      <p class="address">2107 /62 Harbour Lane<br>Sydney, NSW , 2000</p>
      <ul class="contact-list">
        <li>
          <svg viewBox="0 0 16 16" aria-label="Phone"><path d="M3 2h3l1 3-2 1c1 2 2 3 4 4l1-2 3 1v3c0 1-1 2-2 2C6 14 2 10 1 4c0-1 1-2 2-2z" fill="#1c1c1c"/></svg>
          1300 555 018
        </li>
        <li>
          <svg viewBox="0 0 16 16" aria-label="Email"><rect x="1" y="3" width="14" height="10" rx="1" fill="#1c1c1c"/><path d="M1.5 4l6.5 5 6.5-5" stroke="#fff" stroke-width="1.3" fill="none"/></svg>
          info@brightquill.com.au
        </li>
        <li>
          <svg viewBox="0 0 16 16" aria-label="Website"><rect x="1" y="1" width="14" height="14" rx="2" fill="#1c1c1c"/><text x="8" y="12" text-anchor="middle" fill="#fff" font-size="10" font-family="Arial, sans-serif">@</text></svg>
          www.brightquill.com.au
        </li>
      </ul>
    </div>
    <div class="band band--teal"></div>
    <div class="band band--green"></div>
  </section>

</main>
</body>
</html>
```